Re-design of Business Card

We require a design for our business card.

Korrim is a supplier of industrial packaging specializing in plastic products. We are undergoing a rebranding to appear more corporate. We have changed our company name to korrim and have a new logo.

I have uploaded our old card design with the previous company name.
Don't copy the current design. We are looking for a new design.

Industry/Entity Type

Manufacturing

Contact Information for Business Card

please don't copy the current design. we are looking for a new design.

Font styles to use
Sans Serif

Colors

Designer to choose colors to be used in the design.

Requirements
Must have
• clean and easy to read.

```html
<!DOCTYPE html>
<html lang="en">
<head>
<meta charset="utf-8">
<title>Korrim Business Card</title>
<link rel="stylesheet" href="https://fonts.googleapis.com/css2?family=Lato:wght@400;700;900&display=swap">
<style>
  :root {
    --orange: #f47b20;
    --white: #ffffff;
    --ink: #1e1e1e;
    --stage: #e9e9e9;
  }
  * { box-sizing: border-box; margin: 0; padding: 0; }
  html, body { width: 1200px; height: 1200px; overflow: hidden; }
  body {
    background: var(--stage);
    font-family: 'Lato', sans-serif;
    position: relative;
  }
  .card {
    position: absolute;
    left: 250px;
    width: 700px;
    height: 400px;
    box-shadow: 0 6px 18px rgba(0,0,0,.18);
  }
  .card-back {
    top: 150px;
    background: var(--orange);
    color: var(--white);
    border-radius: 90px 0 90px 0;
  }
  .card-front {
    top: 620px;
    background: var(--white);
    color: var(--ink);
    border-radius: 0 90px 0 90px;
  }
  .service-group { position: absolute; }
  .service-title { font-weight: 700; font-size: 19px; margin-bottom: 4px; }
  .service-list { list-style: none; font-size: 16px; line-height: 1.3; padding-left: 8px; }
  .service-list li::before { content: "• "; }
  .group-pallet { left: 60px; top: 40px; }
  .group-flexible { left: 60px; top: 155px; }
  .group-machinery { left: 330px; top: 185px; }
  .group-general { left: 330px; top: 318px; }
  .badges {
    position: absolute; left: 380px; top: 52px;
    display: flex; gap: 22px;
  }
  .badge { width: 84px; height: 84px; border-radius: 50%; background: var(--white); }
  .holder { position: absolute; left: 55px; top: 45px; }
  .holder-name { color: var(--orange); font-weight: 700; font-size: 24px; letter-spacing: .5px; }
  .holder-role { font-size: 17px; }
  .brand-name {
    position: absolute; right: 70px; top: 110px;
    color: var(--orange); font-weight: 900; font-size: 64px; letter-spacing: 2px;
  }
  .contact-list {
    position: absolute; left: 55px; top: 200px;
    list-style: none; font-size: 18px; line-height: 1.35;
  }
  .contact-list li { display: flex; align-items: center; gap: 10px; }
  .contact-list svg { width: 16px; height: 16px; fill: var(--orange); flex: none; }
  .office {
    position: absolute; right: 70px; bottom: 45px; text-align: right; font-size: 18px; line-height: 1.3;
  }
  .office-label { color: var(--orange); font-size: 19px; letter-spacing: .5px; }
</style>
</head>
<body>

<section class="card card-back">
  <div class="service-group group-pallet">
    <h2 class="service-title">Pallet Containment</h2>
    <ul class="service-list">
      <li>Strech</li>
      <li>Heat Shrink</li>
      <li>Pallet Hood</li>
    </ul>
  </div>
  <div class="service-group group-flexible">
    <h2 class="service-title">Flexible Packaging</h2>
    <ul class="service-list">
      <li>Bags &amp; Liners</li>
      <li>Tube</li>
      <li>Film &amp; Sheet</li>
      <li>Printed films</li>
      <li>Shrink Films</li>
    </ul>
  </div>
  <div class="badges">
    <span class="badge"></span>
    <span class="badge"></span>
    <span class="badge"></span>
  </div>
  <div class="service-group group-machinery">
    <h2 class="service-title">Pallet Wrapping Machinery</h2>
    <ul class="service-list">
      <li>Semi &amp; Fully Auto lines</li>
      <li>Finance options</li>
      <li>include lease,Rent,pay per wrap</li>
    </ul>
  </div>
  <div class="service-group group-general">
    <h2 class="service-title">General Packaging</h2>
  </div>
</section>

<section class="card card-front">
  <div class="holder">
    <p class="holder-name">DANA WHITFORD</p>
    <p class="holder-role">Machinery Sales Manager</p>
  </div>
  <p class="brand-name">KORRIM</p>
  <ul class="contact-list">
    <li><svg viewBox="0 0 16 16"><path d="M1 5c0-2 2-3 7-3s7 1 7 3v1h-4V5H5v1H1zM3 7h10l1 7H2z"/></svg>1300 418 260</li>
    <li><svg viewBox="0 0 16 16"><path d="M4 0h8a1 1 0 0 1 1 1v14a1 1 0 0 1-1 1H4a1 1 0 0 1-1-1V1a1 1 0 0 1 1-1zm1 2v10h6V2z"/></svg>XXXX XXX XXX</li>
    <li><svg viewBox="0 0 16 16"><path d="M4 1h8v4H4zM1 6h14v6h-3v3H4v-3H1zm5 5v2h4v-2z"/></svg>+61 7 3854 2917</li>
    <li><svg viewBox="0 0 16 16"><path d="M0 3h16v10H0zm1.5 1.2L8 9l6.5-4.8V4h-13z"/></svg>dana@korrim.com.au</li>
    <li><svg viewBox="0 0 16 16"><circle cx="8" cy="8" r="7.5"/></svg>www.halvorpack.com.au</li>
  </ul>
  <div class="office">
    <p class="office-label">HEAD OFFICE</p>
    <p>58 Carrow St Millbrook</p>
    <p>Qld 4127 Australia</p>
  </div>
</section>

</body>
</html>
```